Need a sleek, professional business card design for a Web Development business

I need a unique business card designed for a web development company. It is also the parent company for any ventures I do, such as my ClipWave channel, startup ideas I have, etc. I am the single member of "Bright Harbor Code LLC." I will attach my basic logo here, so you will see the current color scheme and have the asset available. Thank you!

Target Market(s)

Startups, SMB's, Professionals

Industry/Entity Type

Business

Font styles to use
Other font styles liked:
• Lovello for headings is what I use, but not necessary.

Colors

Designer to choose colors to be used in the design.

Requirements
Nice to have
• Sleek is the word. Professional, modern, dark.
Should not have
• Any work from someone else's design. Lacking originality.

```html
<!DOCTYPE html>
<html lang="en">
<head>
<meta charset="utf-8">
<title>Bright Harbor Code LLC – Business Card</title>
<link href="https://fonts.googleapis.com/css2?family=Open+Sans:wght@300;400;600&display=swap" rel="stylesheet">
<style>
  :root {
    --bg: #e9e6e1;
    --card: #fbfbfb;
    --card-shade: #eeeeee;
    --dark: #1f1f21;
    --orange: #f2a65a;
    --pink: #e8636b;
    --ink: #3a3a3c;
    --rule: #8c8c8c;
  }
  html, body {
    margin: 0;
    padding: 0;
    width: 1200px;
    height: 1023px;
    overflow: hidden;
    background: var(--bg);
  }
  .canvas {
    width: 1200px;
    height: 1023px;
    display: flex;
    align-items: center;
    justify-content: center;
  }
  .business-card {
    width: 1000px;
    height: 572px;
    filter: drop-shadow(0 18px 30px rgba(0,0,0,.18));
  }
  .business-card text { font-family: "Open Sans", Arial, sans-serif; }
  .holder-name { font-size: 46px; font-weight: 600; letter-spacing: 2px; fill: var(--orange); }
  .holder-role { font-size: 25px; font-weight: 400; fill: var(--ink); }
  .address { font-size: 25px; font-weight: 300; fill: var(--ink); }
  .company-name { font-size: 19px; font-weight: 600; fill: var(--pink); letter-spacing: .5px; }
  .contact { font-size: 27px; font-weight: 300; fill: var(--ink); }
  .contact-accent { fill: var(--orange); font-weight: 400; }
  .icon { fill: none; stroke: var(--orange); stroke-width: 2; }
</style>
</head>
<body>
<main class="canvas">
  <svg class="business-card" viewBox="0 0 1000 572" xmlns="http://www.w3.org/2000/svg" aria-label="Bright Harbor Code LLC business card front">
    <defs>
      <linearGradient id="card-surface" x1="0" y1="0" x2="1" y2="1">
        <stop offset="0" stop-color="#ffffff"/>
        <stop offset="1" stop-color="#ececec"/>
      </linearGradient>
      <linearGradient id="accent-line" x1="0" y1="0" x2="1" y2="0">
        <stop offset="0" stop-color="#e8636b"/>
        <stop offset="1" stop-color="#f2a65a"/>
      </linearGradient>
      <clipPath id="card-shape"><rect width="1000" height="572" rx="16"/></clipPath>
    </defs>

    <g clip-path="url(#card-shape)">
      <rect class="card-base" width="1000" height="572" fill="url(#card-surface)"/>

      <!-- dark lower band with step -->
      <path class="dark-band" d="M0 556 L600 556 C640 556 650 510 690 510 L1000 510 L1000 572 L0 572 Z" fill="var(--dark)"/>
      <!-- accent line above band -->
      <path class="accent-stroke" d="M0 548 L598 548 C628 548 640 530 648 518" fill="none" stroke="url(#accent-line)" stroke-width="5"/>
    </g>

    <!-- brand block -->
    <rect class="brand-square" x="62" y="170" width="220" height="200" rx="14" fill="var(--dark)"/>
    <text class="company-name" x="62" y="404">BRIGHT HARBOR CODE LLC.</text>

    <!-- holder -->
    <text class="holder-name" x="930" y="108" text-anchor="end">MARLO KESSEL</text>
    <text class="holder-role" x="930" y="144" text-anchor="end">Managing Partner</text>
    <line class="divider" x1="330" y1="166" x2="930" y2="166" stroke="var(--rule)" stroke-width="1.2" transform="rotate(0)"/>
    <line class="divider-long" x1="330" y1="166" x2="330" y2="166"/>
    <text class="address" x="930" y="212" text-anchor="end">Ufergasse 14, 68723</text>
    <text class="address" x="930" y="248" text-anchor="end">Lindenau, Germany</text>

    <!-- contacts -->
    <line class="contact-rule" x1="330" y1="166" x2="330" y2="166"/>
    <line x1="340" y1="390" x2="700" y2="390" stroke="var(--rule)" stroke-width="1.2"/>
    <g class="contacts">
      <path class="icon" d="M354 420 q-6 6 0 14 q6 8 14 2"/>
      <text class="contact" x="385" y="434">+49 176 480 217 64</text>
      <rect class="icon" x="352" y="452" width="16" height="12" rx="1"/>
      <path class="icon" d="M352 453 l8 6 l8 -6"/>
      <text class="contact" x="385" y="468">info@brightharborcode.com</text>
      <circle class="icon" cx="360" cy="495" r="8"/>
      <text class="contact" x="385" y="502">www.<tspan class="contact-accent">brightharborcode</tspan>.com</text>
    </g>
  </svg>
</main>
</body>
</html>
```